New Label Design Project for Tinkers den wines

I would like to purchase a customized version of a design you have previously submitted - https://www.artmarketfolio.com.au/design/57302946

We need a label that that we can use for our new vintage shiraz, Merlot and Pinot Noir products. This Label will be just 1 label that will be front and back label.
Please see attached

Target Market(s)

young and old wine drinkers

Industry/Entity Type

Wine

Colors

Designer to choose colors to be used in the design.

Requirements
Must have
• logo but also is a bit funky
Nice to have
• mixture of Funky and Modern

```html
<!DOCTYPE html>
<html lang="en">
<head>
<meta charset="utf-8">
<title>Tinkers Den Shiraz Label</title>
<link href="https://fonts.googleapis.com/css2?family=Oswald:wght@300;400;500&display=swap" rel="stylesheet">
<style>
  :root {
    --backdrop: #3a3b40;
    --label-white: #ffffff;
    --label-black: #0d0d0d;
    --accent-red: #d41414;
    --type-white: #f4f4f4;
  }
  * { margin: 0; padding: 0; box-sizing: border-box; }
  html, body {
    width: 1200px;
    height: 900px;
    overflow: hidden;
    background: var(--backdrop);
  }
  .canvas {
    position: relative;
    width: 1200px;
    height: 900px;
  }
  .label {
    position: absolute;
    left: 280px;
    top: 38px;
    width: 640px;
    height: 824px;
    background: var(--label-white);
    padding: 24px;
  }
  .label-face {
    position: relative;
    width: 592px;
    height: 776px;
    background: var(--label-white);
  }
  .label-shapes {
    position: absolute;
    inset: 0;
    width: 100%;
    height: 100%;
  }
  .label-shapes path { fill: var(--label-black); }

  .brand-name {
    position: absolute;
    top: 118px;
    left: 0;
    right: 0;
    text-align: center;
    font-family: "Oswald", sans-serif;
    font-weight: 400;
    font-size: 34px;
    letter-spacing: 3px;
    color: var(--type-white);
  }

  .ship-emblem {
    position: absolute;
    left: 368px;
    top: 246px;
    width: 208px;
    height: 126px;
    background: var(--accent-red);
    border-radius: 4px 4px 18px 40px;
  }

  .wine-details {
    position: absolute;
    left: 0;
    right: 0;
    top: 470px;
    text-align: center;
    font-family: "Oswald", sans-serif;
    color: var(--type-white);
  }
  .varietal {
    font-weight: 500;
    font-size: 62px;
    line-height: 1;
    letter-spacing: 9px;
    padding-left: 9px;
  }
  .region {
    font-weight: 300;
    font-size: 27px;
    line-height: 1;
    letter-spacing: 6px;
    padding-left: 6px;
    margin-top: 4px;
  }
  .vintage {
    display: inline-flex;
    flex-direction: column;
    align-items: center;
    justify-content: center;
    width: 34px;
    height: 56px;
    border: 2px solid var(--accent-red);
    color: var(--accent-red);
    font-weight: 400;
    font-size: 20px;
    line-height: 0.95;
    margin-top: 46px;
  }
  .origin {
    font-weight: 400;
    font-size: 13px;
    letter-spacing: 2px;
    margin-top: 38px;
  }
</style>
</head>
<body>
  <div class="canvas">
    <div class="label">
      <div class="label-face">
        <svg class="label-shapes" viewBox="0 0 498 649" preserveAspectRatio="none" aria-hidden="true">
          <path d="M0 0 H498 V322 L110 290 C40 284 0 250 0 190 Z"/>
          <path d="M498 326 V649 H0 V470 C0 385 40 336 110 333 Z"/>
        </svg>

        <div class="brand-name">Tinkers Den</div>

        <div class="ship-emblem" role="img" aria-label="Red sailing ship emblem"></div>

        <div class="wine-details">
          <div class="varietal">SHIRAZ</div>
          <div class="region">MT. BENSON</div>
          <div class="vintage"><span>20</span><span>07</span></div>
          <div class="origin">WINE OF AUSTRALIA</div>
        </div>
      </div>
    </div>
  </div>
</body>
</html>
```